Business Card Design

We need a business card designed to the point of print ready to take to our printers. the design should be professional, easy to read and simple. The cards should represent our business as professional and trust worthy.

Attached are several versions o the logo, and also the details for the card to be printed. please do communicate if different versions of the logo is required.

Industry/Entity Type

Business

```html
<!DOCTYPE html>
<html lang="en">
<head>
<meta charset="utf-8">
<title>RecoverRight Business Card</title>
<link href="https://fonts.googleapis.com/css2?family=Arimo:wght@400;700&display=swap" rel="stylesheet">
<style>
  :root {
    --ink: #2a2a2a;
    --brand-grey: #5b5b5d;
    --accent: #e3871a;
    --band-top: #8c8c8e;
    --band-bottom: #5c5c5e;
    --rule: #9a9a9a;
    --paper: #ffffff;
  }
  html, body {
    margin: 0;
    padding: 0;
    width: 1200px;
    height: 1000px;
    overflow: hidden;
    background: var(--paper);
    font-family: "Arimo", Arial, sans-serif;
  }
  .card {
    position: absolute;
    left: 104px;
    top: 214px;
    width: 993px;
    height: 568px;
    box-sizing: border-box;
    border: 2px solid #111;
    background: var(--paper);
    overflow: hidden;
  }
  .card-band {
    position: absolute;
    left: 0;
    top: 0;
  }
  .wordmark {
    position: absolute;
    right: 78px;
    top: 76px;
    margin: 0;
    font-size: 48px;
    font-weight: 700;
    color: var(--brand-grey);
    letter-spacing: -0.5px;
    white-space: nowrap;
  }
  .person {
    position: absolute;
    left: 77px;
    top: 158px;
  }
  .person-name {
    margin: 0;
    font-size: 28px;
    font-weight: 400;
    color: var(--ink);
    line-height: 36px;
  }
  .person-role {
    margin: 0;
    font-size: 21px;
    color: var(--accent);
    line-height: 28px;
  }
  .contacts {
    position: absolute;
    left: 74px;
    top: 266px;
    list-style: none;
    margin: 0;
    padding: 0;
  }
  .contacts::after {
    content: "";
    position: absolute;
    left: 37px;
    top: 0;
    width: 1px;
    height: 80px;
    background: var(--rule);
  }
  .contact-item {
    display: flex;
    align-items: center;
    height: 27px;
    margin-bottom: 27px;
    font-size: 21px;
    color: var(--ink);
  }
  .contact-icon {
    width: 24px;
    height: 20px;
    margin-right: 27px;
    flex: none;
  }
  .postal {
    position: absolute;
    left: 77px;
    top: 392px;
    margin: 0;
    font-size: 21px;
    color: var(--ink);
  }
  .web {
    position: absolute;
    left: 22px;
    top: 515px;
    margin: 0;
    font-size: 23px;
    color: #ffffff;
  }
</style>
</head>
<body>
  <div class="card">
    <svg class="card-band" width="989" height="564" viewBox="0 0 989 564" aria-hidden="true">
      <defs>
        <linearGradient id="bandShade" x1="0" y1="0" x2="0" y2="1">
          <stop offset="0" stop-color="var(--band-top)"/>
          <stop offset="1" stop-color="var(--band-bottom)"/>
        </linearGradient>
      </defs>
      <polygon points="0,494 377,494 474,542 989,542 989,564 0,564" fill="url(#bandShade)"/>
      <polygon points="396,494 989,494 989,510" fill="var(--accent)"/>
      <polygon points="466,520 989,520 989,535" fill="var(--accent)"/>
    </svg>

    <p class="wordmark">RecoverRight Pty Ltd</p>

    <div class="person">
      <h1 class="person-name">Hannah Torvik</h1>
      <p class="person-role">Managing Director</p>
    </div>

    <ul class="contacts">
      <li class="contact-item">
        <svg class="contact-icon" viewBox="0 0 24 20" aria-label="Phone">
          <path d="M2 8 C2 3 22 3 22 8 L22 10 L17 10 L17 7 L7 7 L7 10 L2 10 Z" fill="var(--accent)"/>
          <path d="M6 11 L18 11 L20 17 L4 17 Z" fill="var(--accent)"/>
          <circle cx="12" cy="14" r="2" fill="#fff"/>
        </svg>
        <span>+61 400 555 019</span>
      </li>
      <li class="contact-item">
        <svg class="contact-icon" viewBox="0 0 24 20" aria-label="Email">
          <rect x="3" y="4" width="18" height="13" fill="none" stroke="var(--accent)" stroke-width="2"/>
          <path d="M3 4 L12 11 L21 4 M3 17 L10 10 M21 17 L14 10" fill="none" stroke="var(--accent)" stroke-width="1.6"/>
        </svg>
        <span>htorvik@recoverright.com.au</span>
      </li>
    </ul>

    <p class="postal">PO Box 2270 Harbour Centre Qld 4100</p>

    <p class="web">www.recoverright.com.au</p>
  </div>
</body>
</html>
```